Simple Floral Service Web-Banner

I need to put a banner add on the members section of a website for an organization in which we are members.

The ad size is 470px x 214px.

I am uploading 4 pictures. 1 is a picture of red roses, and 1 is a picture of a t-shirt. These are 2 major products of ours which need to be incorporated in the banner. I do not have these in higher res or vectorized format, so please work with what you have. I am also uploading our 2 logos, one is for our Canadian company, and one for our American company. Both logos should be included at equal sizes.

The following text should be used:
"Proudly providing top quality roses, and custom commemorative grad t-shirts at over 800 schools."

I am just looking for a simple banner incorporating those pictures and that wording. I don't want something that is overly flashy.

I will monitor the submissions in a timely manner and give you feedback.

```html
<!DOCTYPE html>
<html lang="en">
<head>
<meta charset="utf-8">
<title>Floral Service Banner</title>
<link rel="stylesheet" href="https://fonts.googleapis.com/css2?family=Roboto+Condensed:wght@400;700&display=swap">
<style>
  :root {
    --page: #ffffff;
    --cream: #fefad6;
    --leaf: #73993d;
    --leaf-text: #76a03a;
    --white: #ffffff;
    --shirt: #d9d9d6;
    --rose: #b3161c;
    --foliage: #4f7a34;
  }
  html, body {
    margin: 0;
    padding: 0;
    width: 1200px;
    height: 1000px;
    overflow: hidden;
    background: var(--page);
  }
  .canvas {
    position: relative;
    width: 1200px;
    height: 1000px;
  }
  .banner {
    position: absolute;
    left: 68px;
    top: 258px;
    width: 1067px;
    height: 486px;
    background: var(--cream);
  }
  .product-shirts {
    position: absolute;
    left: 0;
    top: 36px;
    width: 354px;
    height: 308px;
    border-radius: 14px;
    background: linear-gradient(160deg, #eeeeec 0%, var(--shirt) 60%, #c7c7c3 100%);
  }
  .product-roses {
    position: absolute;
    left: 750px;
    top: 80px;
    width: 317px;
    height: 258px;
    border-radius: 20px;
    background: radial-gradient(ellipse at 60% 45%, var(--rose) 0%, #c8282c 35%, var(--foliage) 75%, #e9ecdf 100%);
  }
  .brands {
    position: absolute;
    left: 372px;
    top: 36px;
    width: 336px;
    font-family: "Roboto Condensed", sans-serif;
    font-weight: 400;
    color: var(--leaf-text);
    text-align: right;
  }
  .brand-name {
    margin: 0;
    font-size: 66px;
    line-height: 64px;
    letter-spacing: -1px;
  }
  .brand-divider {
    height: 3px;
    margin: 12px 0 14px;
    background: var(--leaf-text);
  }
  .tagline-band {
    position: absolute;
    left: 0;
    bottom: 0;
    width: 1067px;
    height: 129px;
    background: var(--leaf);
    display: flex;
    align-items: center;
    justify-content: center;
  }
  .tagline {
    margin: 0;
    font-family: "Roboto Condensed", sans-serif;
    font-weight: 700;
    font-size: 41px;
    line-height: 48px;
    color: var(--white);
    text-align: center;
  }
</style>
</head>
<body>
<div class="canvas">
  <section class="banner">
    <div class="product-shirts" role="img" aria-label="Photo of front and back of white commemorative grad t-shirts with school name and graduating class list"></div>

    <div class="brands">
      <p class="brand-name">Milestone<br>Flowers</p>
      <div class="brand-divider"></div>
      <p class="brand-name">Laureate<br>Flowers</p>
    </div>

    <div class="product-roses" role="img" aria-label="Photo of a bouquet of red roses with baby's breath wrapped in white paper"></div>

    <div class="tagline-band">
      <p class="tagline">Proudly Providing Top Quality Roses, and Custom<br>Commemorative Grad T-shirts at Over 800 Schools.</p>
    </div>
  </section>
</div>
</body>
</html>
```